Business Card Design

I need a business card design for my new solo law practice. I practice consumer bankruptcy law.

I would like a simple, functional business card that looks professional but will also be understandable to regular people - not just other lawyers.
Updates

I added a couple of possible logos that can be incorporated

I'm sorry about the confusion, but the suite number for my new office is suite #150. Thanks for your patience

Target Market(s)

the real target market is potential clients

Industry/Entity Type

Business

Contact Information for Business Card

Law Offices of Theodore M. Vance
Theodore M. Vance
Attorney at Law
Bankruptcy Law
418 Marlowe Court #150
Johnstown, PA 15901
(555) 317-6482 (Phone)
(555) 317-6497 (Fax)
theov@cedarpointdebtrelief.example
cedarpointdebtrelief.example

Font styles to use
Serif

Requirements
Nice to have
• I've added some possible logos to possible incorporate

```html
<!DOCTYPE html>
<html lang="en">
<head>
<meta charset="utf-8">
<title>Law Offices of Theodore M. Vance – Business Card</title>
<link rel="stylesheet" href="https://fonts.googleapis.com/css2?family=Arimo:wght@400;700&display=swap">
<style>
  :root {
    --page: #ffffff;
    --parchment-light: #dccfae;
    --parchment-mid: #cfbf98;
    --parchment-dark: #bfae86;
    --band: #1f0f0d;
    --band-edge: #f3bb8c;
    --mark: #dcc8a4;
    --band-text: #dbc49e;
    --ink: #141010;
    --rule: #111111;
    --ornament: #3a1f12;
  }
  * { margin: 0; padding: 0; box-sizing: border-box; }
  html, body {
    width: 1200px;
    height: 664px;
    overflow: hidden;
    background: var(--page);
  }
  .card {
    position: absolute;
    left: 61px;
    top: 19px;
    width: 1079px;
    height: 614px;
    background:
      radial-gradient(ellipse at 30% 30%, var(--parchment-light) 0%, transparent 60%),
      radial-gradient(ellipse at 75% 80%, var(--parchment-dark) 0%, transparent 55%),
      var(--parchment-mid);
    overflow: hidden;
    font-family: "Arimo", Arial, sans-serif;
  }
  .frame-lines {
    position: absolute;
    inset: 0;
    width: 1079px;
    height: 614px;
  }
  .ornament {
    position: absolute;
    border-radius: 50%;
    background: radial-gradient(ellipse at center, rgba(58,31,18,0.55) 0%, rgba(58,31,18,0.25) 45%, rgba(58,31,18,0) 72%);
  }
  .ornament--top-right { left: 835px; top: 4px; width: 230px; height: 215px; }
  .ornament--bottom-left { left: 4px; top: 375px; width: 245px; height: 235px; }
  .name-band {
    position: absolute;
    left: 40px;
    top: 216px;
    width: 1016px;
    height: 159px;
    background: var(--band);
    border: 6px solid var(--band-edge);
    text-align: center;
  }
  .monogram {
    position: absolute;
    left: 0; right: 0;
    top: 18px;
    font-weight: 700;
    font-size: 70px;
    line-height: 1;
    color: var(--mark);
    letter-spacing: 1px;
  }
  .firm-name {
    position: absolute;
    left: 0; right: 0;
    top: 99px;
    font-size: 18px;
    color: var(--band-text);
  }
  .firm-rule {
    position: absolute;
    left: 326px;
    top: 126px;
    width: 372px;
    height: 2px;
    background: var(--band-text);
  }
  .contact {
    position: absolute;
    left: 0;
    width: 1099px;
    top: 383px;
    text-align: center;
    color: var(--ink);
    font-size: 21px;
    line-height: 29px;
  }
  .contact .phone { font-weight: 700; }
  .contact .gap { margin-top: 5px; }
</style>
</head>
<body>
  <div class="card">
    <svg class="frame-lines" viewBox="0 0 1079 614" aria-hidden="true">
      <polyline points="44,197 44,25 859,25" fill="none" stroke="var(--rule)" stroke-width="2"/>
      <polyline points="216,572 1035,572 1035,384" fill="none" stroke="var(--rule)" stroke-width="2"/>
    </svg>

    <div class="ornament ornament--top-right" role="img" aria-label="Floral vine ornament in dark brown"></div>
    <div class="ornament ornament--bottom-left" role="img" aria-label="Floral vine ornament in dark brown"></div>

    <div class="name-band">
      <div class="monogram">TMV</div>
      <div class="firm-name">Law Offices of Theodore M. Vance</div>
      <div class="firm-rule"></div>
    </div>

    <div class="contact">
      <p>Theodore M. Vance Attorney at Law Bankruptcy Law</p>
      <p>418 Marlowe Court #150 Johnstown, PA 15901</p>
      <p class="phone gap">(555) 317-6482 (Phone)</p>
      <p class="phone">(555) 317-6497 (Fax)</p>
      <p>theov@cedarpointdebtrelief.example</p>
      <p>cedarpointdebtrelief.example</p>
    </div>
  </div>
</body>
</html>
```